Business Card Design

redesign of card and recreation of logo based on image provided. the business is located in new york so the Halvard Bridge figures prominently in the scheme. product should be very clean.

Industry/Entity Type

Real Estate

Contact Information for Business Card

Owen Tillbury 318 Dellmont Avenue Eastmere, NR 40912 owen@kestrelrow.example Mobile: 646-555-0193

Colors
cadf82
1b1b1b
ffffff

Requirements
Nice to have
• Halvard Bridge

```html
<!DOCTYPE html>
<html lang="en">
<head>
<meta charset="utf-8">
<title>Kestrel Row Realty — Business Card</title>
<link rel="stylesheet" href="https://fonts.googleapis.com/css2?family=Josefin+Sans:wght@300;400&display=swap">
<style>
  :root {
    --lime: #cadf82;
    --ink: #1b1b1b;
    --paper: #ffffff;
    --stage: #c9dc86;
    --sketch-light: #d9d9d9;
    --sketch-dark: #8a8a8a;
  }
  * { box-sizing: border-box; margin: 0; padding: 0; }
  html, body { width: 1200px; height: 750px; overflow: hidden; }
  body {
    background: var(--stage);
    font-family: "Josefin Sans", "Helvetica Neue", Arial, sans-serif;
    font-weight: 300;
    color: var(--ink);
    position: relative;
  }
  .card {
    position: absolute;
    top: 226px;
    width: 520px;
    height: 297px;
    background: var(--paper);
    border-radius: 24px;
  }
  .card--front { left: 60px; }
  .card--back { left: 620px; }

  /* Front */
  .bridge-art {
    position: absolute;
    background: linear-gradient(135deg, var(--sketch-light), var(--sketch-dark));
  }
  .card--front .bridge-art {
    left: 200px; top: 62px;
    width: 120px; height: 70px;
  }
  .wordmark {
    position: absolute;
    left: 0; right: 0;
    top: 158px;
    text-align: center;
    font-size: 34px;
    letter-spacing: 1px;
    text-transform: uppercase;
    color: var(--ink);
    line-height: 1;
  }
  .tagline {
    position: absolute;
    left: 0; right: 0;
    top: 204px;
    text-align: center;
    font-size: 10px;
    letter-spacing: 6px;
    text-transform: uppercase;
    color: var(--lime);
  }

  /* Back */
  .card--back .bridge-art {
    left: 250px; top: 22px;
    width: 20px; height: 12px;
  }
  .wordmark--small {
    top: 40px;
    font-size: 9px;
    letter-spacing: 0.8px;
  }
  .holder {
    position: absolute;
    left: 0; right: 0;
    top: 78px;
    text-align: center;
  }
  .holder__name {
    font-size: 30px;
    text-transform: uppercase;
    letter-spacing: 0.5px;
    line-height: 1;
  }
  .holder__role {
    font-size: 15px;
    text-transform: uppercase;
    color: var(--lime);
    margin-top: 6px;
    letter-spacing: 0.5px;
  }
  .contact {
    position: absolute;
    display: flex;
    align-items: center;
    gap: 8px;
    font-size: 11px;
    font-weight: 400;
    line-height: 1.3;
  }
  .contact svg { flex: none; }
  .contact--email { left: 330px; top: 150px; }
  .contact--phone { left: 200px; top: 182px; }
  .contact--address { left: 32px; top: 238px; }
  .website {
    position: absolute;
    left: 0; right: 0; top: 214px;
    text-align: center;
    font-size: 11px;
    font-weight: 400;
    letter-spacing: 0.5px;
    text-transform: uppercase;
    color: var(--lime);
  }
</style>
</head>
<body>

<section class="card card--front" aria-label="Card front">
  <div class="bridge-art" role="img" aria-label="Pen sketch of the Halvard Bridge"></div>
  <p class="wordmark">Kestrel Row Realty</p>
  <p class="tagline">Real Estate</p>
</section>

<section class="card card--back" aria-label="Card back">
  <div class="bridge-art" role="img" aria-label="Small sketch of the Halvard Bridge"></div>
  <p class="wordmark wordmark--small">Kestrel Row Realty</p>

  <div class="holder">
    <p class="holder__name">Owen Tillbury</p>
    <p class="holder__role">Broker</p>
  </div>

  <p class="contact contact--email">
    <svg width="12" height="12" viewBox="0 0 12 12" aria-hidden="true">
      <circle cx="6" cy="6" r="5.3" fill="none" stroke="var(--lime)" stroke-width="1.2"/>
      <rect x="3.3" y="4" width="5.4" height="4" fill="none" stroke="var(--lime)" stroke-width="0.9"/>
      <path d="M3.3 4 L6 6.2 L8.7 4" fill="none" stroke="var(--lime)" stroke-width="0.9"/>
    </svg>
    owen@kestrelrow.example
  </p>

  <p class="contact contact--phone">
    <svg width="12" height="12" viewBox="0 0 12 12" aria-hidden="true">
      <circle cx="6" cy="6" r="5.3" fill="none" stroke="var(--lime)" stroke-width="1.2"/>
      <path d="M4 3.4 L5 3.4 L5.5 4.8 L4.9 5.3 Q5.6 6.6 6.7 7.1 L7.2 6.5 L8.6 7 L8.6 8 Q6.8 8.5 5.3 7 Q3.7 5.4 4 3.4 Z" fill="var(--lime)"/>
    </svg>
    646-555-0193
  </p>

  <p class="website">www.kestrelrow.example</p>

  <p class="contact contact--address">
    <svg width="12" height="12" viewBox="0 0 12 12" aria-hidden="true">
      <circle cx="6" cy="6" r="5.3" fill="none" stroke="var(--lime)" stroke-width="1.2"/>
      <path d="M6 9 L4.2 6 A2 2 0 1 1 7.8 6 Z" fill="var(--lime)"/>
      <circle cx="6" cy="5.1" r="0.7" fill="var(--paper)"/>
    </svg>
    <span>318 Dellmont Avenue<br>Eastmere, NR 40912</span>
  </p>
</section>

</body>
</html>
```